Stonefield Crafters Brochure = SCC $$$

this brochure will be used for a canvassing campaign (door to door) appointment setting

the campaign will be for homeowners that would like to do any kind of improvement to their house - home improvement
from EXT paint or roof repair all the way to kitchen and bathroom remodeling

we want to catch the prospect eye with the brochure and to educate our prospect about the different ways they could improve their house step by step to their dream house

Target Market(s)

Homeowners
anyone who would like to improve or fix any part of their house

Industry/Entity Type

Home Improvement

Contact Information for Business Card

the green roof house blueprints on one side
the Stonefield Crafters logo on the other side

Font styles to use
Serif
Decorative

Colors
ffffff
886aae
9bcb3b
e6e6e6

Requirements
Must have
• this is a TRI-FOLD brochure
• call for action -- schedule your free estimate
• or any idea that will lead to set up an appointment with our specialist
• LOOK AT MY WEBSITE TO UNDERSTAND MORE WHAT I LIKE
• WWW.STONEFIELDCRAFTERSCO.EXAMPLE
• services:
• Kitchen Renovations
• Bathroom Renovations
• Modern Landscaping
• Additions + in-law quarters
• Exterior paint +interior paint
• wood replacement + stucco repair
• roof repair
• railling and glass work
Nice to have
• the pictures I have uploaded can use as an example but im open to other ideas...
• THERE IS NO SUBSTITUTE FOR QUALITY.
• the picture of the women in the kitchen--
• i enjoy making food and spending time in my new kitchen, to see my whole family sitting down to eat dinner together in our perfect little kitchen make me so happy
Should not have
• the 2 brochures i have uploaded are for example only

```html
<!DOCTYPE html>
<html lang="en">
<head>
<meta charset="utf-8">
<title>Stonefield Crafters Tri-fold Brochure</title>
<link href="https://fonts.googleapis.com/css2?family=Cinzel:wght@700&family=Lato:wght@400;700;900&display=swap" rel="stylesheet">
<style>
  :root{
    --white:#ffffff;
    --purple:#886aae;
    --green:#9bcb3b;
    --grey:#e6e6e6;
    --ink:#1b1b1b;
    --text:#4a4a4a;
    --serif:"Cinzel", Georgia, serif;
    --sans:"Lato", Arial, sans-serif;
  }
  *{box-sizing:border-box;margin:0;padding:0}
  html,body{width:1200px;height:1200px;overflow:hidden}
  body{background:#d9d9d9;font-family:var(--sans);color:var(--text);position:relative}
  .sheet{position:absolute;left:180px;width:840px;height:560px;background:var(--white);overflow:hidden;box-shadow:0 4px 14px rgba(0,0,0,.18)}
  .sheet--outside{top:27px}
  .sheet--inside{top:613px}
  .sheet .art{position:absolute;inset:0;width:840px;height:560px}
  .fold{position:absolute;top:0;bottom:0;width:1px;background:rgba(0,0,0,.06)}
  .photo{position:absolute}
  .tag{position:absolute;display:flex;align-items:center;gap:5px;height:18px;padding:0 10px 0 2px;background:var(--purple);color:var(--white);border-radius:9px;font:700 10px/1 var(--sans)}
  .tag i{display:block;width:14px;height:14px;border-radius:50%;background:var(--white)}
  .heading{position:absolute;color:var(--purple);font:900 12px/1 var(--sans);letter-spacing:.5px;text-transform:uppercase}
  .copy{position:absolute;font:400 9.5px/1.4 var(--sans);color:var(--text)}
  .brand{position:absolute;display:flex;align-items:center;gap:8px}
  .brand .dot{width:26px;height:26px;border-radius:50%;background:var(--ink)}
  .brand span{font:700 14px/1 var(--serif);color:var(--ink);letter-spacing:1px}
  .contact{position:absolute;left:300px;width:240px;text-align:center;font:700 9.5px/1.35 var(--sans);color:var(--ink)}
  .contact .ico{display:block;margin:0 auto 3px;width:14px;height:14px}
  .badge{position:absolute;left:370px;top:350px;width:120px;height:120px;border-radius:50%;background:var(--white);border:5px solid var(--green);display:flex;flex-direction:column;align-items:center;justify-content:center;text-align:center;line-height:1}
  .badge .s{color:var(--purple);font:700 12px var(--sans)}
  .badge .y{color:var(--purple);font:700 12px var(--sans);text-transform:uppercase;letter-spacing:1px;margin-top:2px}
  .badge .f{color:var(--green);font:900 28px var(--sans);margin-top:2px}
  .badge .e{color:var(--purple);font:700 15px var(--sans)}
  .slogan{position:absolute;left:585px;top:395px;width:240px;font:700 20px/1.15 var(--serif);color:var(--white)}
  .slogan .accent{display:block;color:var(--green);font-size:26px}
  .site{position:absolute;left:585px;top:505px;font:400 9px/1 var(--sans);color:var(--white);letter-spacing:.5px}
</style>
</head>
<body>

<section class="sheet sheet--outside" aria-label="Brochure outside spread">
  <svg class="art" viewBox="0 0 840 560">
    <defs>
      <linearGradient id="roofer" x1="0" y1="0" x2="1" y2="1">
        <stop offset="0" stop-color="#4a7fc4"/><stop offset=".55" stop-color="#2f5fa8"/><stop offset="1" stop-color="#d27c4d"/>
      </linearGradient>
      <linearGradient id="house" x1="0" y1="0" x2="0" y2="1">
        <stop offset="0" stop-color="#cfdbe6"/><stop offset=".55" stop-color="#eef0f0"/><stop offset="1" stop-color="#9ea39e"/>
      </linearGradient>
    </defs>
    <polygon role="img" aria-label="Photo of a roofer with hard hat hammering shingles on a roof" points="0,560 0,390 400,390 560,320 560,560" fill="url(#roofer)"/>
    <polyline points="400,390 560,320" fill="none" stroke="var(--green)" stroke-width="5"/>
    <rect role="img" aria-label="Photo of a modern white two-storey house with palm trees" x="560" y="55" width="280" height="290" fill="url(#house)"/>
    <polygon points="560,300 650,330 840,330 840,345 650,345 560,315" fill="var(--green)"/>
    <polygon points="560,315 650,345 840,345 840,560 560,560" fill="#161616"/>
  </svg>
  <div class="fold" style="left:280px"></div>
  <div class="fold" style="left:560px"></div>

  <div class="tag" style="left:18px;top:18px"><i></i>Roof repair</div>
  <svg class="photo" style="left:18px;top:44px" width="244" height="120"><rect role="img" aria-label="Photo of workers repairing a roof beside a brick chimney" width="244" height="120" fill="#8fb0c9"/></svg>
  <div class="tag" style="left:18px;top:180px"><i></i>Railing and glass work</div>
  <svg class="photo" style="left:18px;top:206px" width="244" height="120"><rect role="img" aria-label="Photo of a worker installing a glass window panel" width="244" height="120" fill="#b9c4cf"/></svg>

  <div class="heading" style="left:300px;top:20px">About us</div>
  <p class="copy" style="left:300px;top:38px;width:240px">We believe that every project deserves the same kind of attention, no matter if it's a one room remodel or a new build of a multimillion dollar structure. To us, quality is achieving the best results with the highest grade material at the lowest cost to you. That is how we define quality and that is what you're getting with Stonefield Crafters. We never use sub-contractors or outsource our jobs.</p>
  <div class="brand" style="left:320px;top:150px"><div class="dot"></div><span>STONEFIELD CRAFTERS</span></div>
  <div class="contact" style="top:192px">
    <svg class="ico" viewBox="0 0 14 14"><circle cx="7" cy="7" r="7" fill="var(--purple)"/><path d="M3.5 7.5 7 4l3.5 3.5V10h-7z" fill="#fff"/></svg>
    Stonefield Crafters<br><span style="font-weight:400">418 Alder Bend Rd. Suite 3<br>Fairhaven, CA 90000</span>
  </div>
  <div class="contact" style="top:250px">
    <svg class="ico" viewBox="0 0 14 14"><circle cx="7" cy="7" r="7" fill="var(--purple)"/><path d="M4.5 3.8h1.6l.7 1.8-1 .8c.5 1 1.2 1.7 2.2 2.2l.8-1 1.8.7v1.6c-3.6.2-6.3-2.5-6.1-6.1z" fill="#fff"/></svg>
    (555) 014-2270
  </div>
  <div class="contact" style="top:283px">
    <svg class="ico" viewBox="0 0 14 14"><circle cx="7" cy="7" r="7" fill="var(--purple)"/><rect x="3.5" y="4.5" width="7" height="5" fill="#fff"/><path d="M3.5 4.5 7 7.3l3.5-2.8" fill="none" stroke="var(--purple)" stroke-width=".8"/></svg>
    <span style="font-weight:400">hello@stonefieldcraftersco.example</span>
  </div>

  <div class="badge"><span class="s">schedule</span><span class="y">your</span><span class="f">FREE</span><span class="e">estimate</span></div>

  <div class="brand" style="left:578px;top:16px"><div class="dot"></div><span>STONEFIELD CRAFTERS</span></div>
  <div class="slogan">THERE IS NO<span class="accent">SUBSTITUTE</span>FOR QUALITY</div>
  <div class="site">WWW.STONEFIELDCRAFTERSCO.EXAMPLE</div>
</section>

<section class="sheet sheet--inside" aria-label="Brochure inside spread">
  <svg class="art" viewBox="0 0 840 560">
    <defs>
      <linearGradient id="kitchen2" x1="0" y1="0" x2="1" y2="1">
        <stop offset="0" stop-color="#f3f1ec"/><stop offset="1" stop-color="#c9c2b4"/>
      </linearGradient>
    </defs>
    <polygon role="img" aria-label="Photo of a bright white kitchen with a man working on cabinets" points="200,560 200,450 560,450 700,318 840,318 840,560" fill="url(#kitchen2)"/>
    <polyline points="560,452 700,320 840,320" fill="none" stroke="var(--green)" stroke-width="5"/>
    <rect role="img" aria-label="Photo of a smiling woman holding a mug in her kitchen" x="0" y="450" width="200" height="110" fill="#c7cfdc"/>
    <rect role="img" aria-label="Photo of a smiling contractor in a blue polo shirt holding a screwdriver" x="690" y="332" width="140" height="228" fill="#5b86c4"/>
  </svg>
  <div class="fold" style="left:280px"></div>
  <div class="fold" style="left:560px"></div>

  <div class="heading" style="left:18px;top:18px">Services:</div>
  <div class="tag" style="left:18px;top:36px"><i></i>Kitchen Renovations</div>
  <p class="copy" style="left:18px;top:60px;width:244px">There is a reason the Kitchen is called "The Heart of the Home." From bustling family breakfasts through baking misadventures covered in flour to soothing late-night conversations over tea, the Kitchen serves as the setting for the primary bonding moments in the home. Shouldn't your Kitchen invite your family in?</p>
  <svg class="photo" style="left:18px;top:150px" width="244" height="118"><rect role="img" aria-label="Photo of a modern kitchen with grey cabinets and a wooden island" width="244" height="118" fill="#7d7f7e"/></svg>
  <div class="tag" style="left:18px;top:284px"><i></i>Bathroom Renovations</div>
  <p class="copy" style="left:18px;top:308px;width:244px">Everyone wants to relax after a long day in a Bathroom that serves as a high-end spa conveniently located in your home. Whether it's taking a steaming shower after a strenuous workout, or unwinding after a long day by soaking in a bubbly bathtub, your Bathroom should be a place of repose and rejuvenation. Let us help you relax.</p>

  <div class="tag" style="left:298px;top:18px"><i></i>Modern Landscaping</div>
  <p class="copy" style="left:298px;top:42px;width:244px">Want to be that neighbor - the one with the amazing lawn that everyone has to stare at before they continue on their way? One of our specialties is embracing California's dry climate to create a Drought-Tolerant Garden - a yard or lawn teeming with a colorful medley of low-maintenance succulents. Good for the planet and eye-catchingly beautiful - sounds like a win-win situation!</p>
  <svg class="photo" style="left:298px;top:150px" width="244" height="104"><rect role="img" aria-label="Photo of landscapers laying turf and planting a garden" width="244" height="104" fill="#8a6c52"/></svg>
  <div class="tag" style="left:298px;top:266px"><i></i>Additions + in-law quarters</div>
  <p class="copy" style="left:298px;top:290px;width:244px">Want to utilize the greatest potential of your premises? Whether it's building guest lodgings to rent out when your bills become overwhelming, or creating a cozy space for friends and family to stay while visiting, sometimes you just need to accommodate more people. A space completely separate from you, yet still yours. Shouldn't you get to benefit from the entirety of your property?</p>
  <div class="brand" style="left:298px;top:408px"><div class="dot"></div><span>STONEFIELD CRAFTERS</span></div>

  <div class="tag" style="left:578px;top:18px"><i></i>Exterior paint + interior paint</div>
  <svg class="photo" style="left:578px;top:44px" width="244" height="108"><rect role="img" aria-label="Photo of painters rolling paint on interior walls" width="244" height="108" fill="#dcdcd6"/></svg>
  <div class="tag" style="left:578px;top:166px"><i></i>Wood replacement + stucco repair</div>
  <svg class="photo" style="left:578px;top:192px" width="244" height="100"><rect role="img" aria-label="Photo of a lit wooden pergola patio at dusk" width="244" height="100" fill="#3d4a6a"/></svg>
</section>

</body>
</html>
```